Business Card Design

We just need these details on one side of card and logo on the other.

Industry/Entity Type

Business

Contact Information for Business Card

Colette Marsh | Artist
87 Tillbrook Lane
Dunmore Heights Vic 3172
# 0418 207 913 | 03 9386 2417
colette@colettemarsh-example.com
colettesstudio-example.com.au

```html
<!DOCTYPE html>
<html lang="en">
<head>
<meta charset="utf-8">
<title>Colette Marsh – Business Card</title>
<link rel="stylesheet" href="https://fonts.googleapis.com/css2?family=Josefin+Sans:wght@300;400&display=swap">
<style>
  :root {
    --backdrop: #e6e4e1;
    --card-black: #0b0b0c;
    --card-edge: #1a1a1c;
    --ink-white: #f2f2f2;
    --ink-silver: #a9a9ab;
    --ink-muted: #8a8a8c;
  }
  * { box-sizing: border-box; margin: 0; padding: 0; }
  html, body {
    width: 924px;
    height: 1200px;
    overflow: hidden;
    background: var(--backdrop);
    font-family: "Josefin Sans", sans-serif;
  }
  .card {
    position: absolute;
    left: 82px;
    width: 760px;
    height: 434px;
    background:
      repeating-linear-gradient(90deg, rgba(255,255,255,0.012) 0 1px, transparent 1px 3px),
      linear-gradient(160deg, var(--card-edge) 0%, var(--card-black) 55%, #050506 100%);
    box-shadow: 0 12px 30px rgba(0,0,0,0.25);
  }
  .card--contact { top: 130px; }
  .card--brand { top: 640px; }

  .identity {
    position: absolute;
    top: 78px;
    right: 68px;
    text-align: right;
    color: var(--ink-white);
  }
  .identity__name {
    font-size: 40px;
    font-weight: 300;
    letter-spacing: 0.06em;
    line-height: 1;
  }
  .identity__role {
    margin-top: 10px;
    font-size: 12px;
    font-weight: 300;
    letter-spacing: 0.9em;
    text-transform: uppercase;
    margin-right: -0.9em;
  }

  .contact {
    position: absolute;
    right: 68px;
    top: 210px;
    list-style: none;
    text-align: right;
    color: var(--ink-white);
    font-size: 17px;
    font-weight: 300;
    letter-spacing: 0.12em;
    line-height: 1.85;
  }
  .contact__small { font-size: 14px; text-transform: uppercase; letter-spacing: 0.14em; }

  .brand {
    position: absolute;
    inset: 0;
    display: flex;
    flex-direction: column;
    align-items: center;
    justify-content: center;
    color: var(--ink-silver);
  }
  .brand__name {
    font-size: 62px;
    font-weight: 300;
    letter-spacing: 0.05em;
    line-height: 1;
  }
  .brand__tagline {
    margin-top: 22px;
    font-size: 17px;
    font-weight: 300;
    letter-spacing: 0.28em;
    text-transform: uppercase;
    color: var(--ink-muted);
  }
  .brand__dot { display: inline-block; margin: 0 0.6em; }
</style>
</head>
<body>

  <section class="card card--contact" aria-label="Business card, contact side">
    <div class="identity">
      <p class="identity__name">Colette Marsh</p>
      <p class="identity__role">Artist</p>
    </div>
    <ul class="contact">
      <li>87 Tillbrook Lane, Dunmore Heights, Vic 3172</li>
      <li>0418 207 913 | 03 9386 2417</li>
      <li class="contact__small">colette@colettemarsh-example.com</li>
      <li class="contact__small">www.colettesstudio-example.com.au</li>
    </ul>
  </section>

  <section class="card card--brand" aria-label="Business card, brand side">
    <div class="brand">
      <p class="brand__name">Colette's Studio</p>
      <p class="brand__tagline">Studio<span class="brand__dot">•</span>Cafe<span class="brand__dot">•</span>Gallery</p>
    </div>
  </section>

</body>
</html>
```